Tri-fold Brochure, Postcard & Letterhead Design | ||
Small Engineering Consulting & Services Firm for Building Energy Efficiency | ||
I want to have tri-fold brochure and postcard designs that can represent our company well. Our company is providing engineering consulting and services to improve energy efficiency of building mechanical systems and thus reduce energy consumptions of large commercial buildings. The details of the company information can be found in the website: www.corvalith.com, and any questions about the can be routed to tkal@corvalith.com. I have my company logo and biz card design in different format (originally designed by Emblem Craft Hub) and provide them to designers upon request. | ||
Building owners and facility managers of commercial, institutional and industrial buildings, including large office buildings, hospitals, schools and university campuses, data centers, etc. | ||
The tri-fold brochure and postcard should be designed in a way that its contents can be editable in MS Publisher or Word. The letter head can be designed for use in MS Word. |
HVAC_system_solutions_728.jpg Hello, designers! As posted in our website www.corvalith.com, our company is providing services to improve building energy efficiency. Our customers are building owners, facility managers and operators. The real focus of our business is to optimize the operation of building mechanical systems. We don't do the lighting ourselves and typically oursource the lighting portion. In a building, mechanical systems consume more than 50% of energy for heating, ventilating and air-conditioning. So I would like to have images related to the building mechanical systems. You may google images of "HVAC", "chillers", "AHU", and/or "building automation systems". I will upload some samples from google images. I hope it can help. Thanks, |
CORVALITH_23480_FinalLogo_D4L4_714.jpg Use the uploaded logo and also reference the business card design. To understand the company's services and characters, check out the company website at www.corvalith.com |

```html
<!DOCTYPE html>
<html lang="en">
<head>
<meta charset="utf-8">
<title>CORVALITH Tri-fold Brochure – Inside</title>
<link href="https://fonts.googleapis.com/css2?family=Open+Sans:wght@400;600;700&display=swap" rel="stylesheet">
<style>
  :root{
    --orange:#ef7d22;
    --green:#5fae3a;
    --blue:#1d5fa3;
    --navy:#16406f;
    --text:#555a60;
    --sky:#7fb6e0;
    --paper:#ffffff;
  }
  *{box-sizing:border-box;margin:0;padding:0}
  html,body{width:1200px;height:965px;overflow:hidden;background:var(--paper)}
  body{font-family:"Open Sans",Arial,sans-serif;color:var(--text);position:relative}
  .panel{position:absolute;top:18px;width:370px;height:832px}
  .panel--services{left:18px}
  .panel--procedure{left:430px}
  .panel--cases{left:822px}
  .panel-head{height:38px;background:var(--orange);display:flex;align-items:center;justify-content:space-between;padding:0 10px 0 12px;border-radius:2px}
  .panel-head h2{color:#fff;font-size:19px;font-weight:700;letter-spacing:.5px}
  .brand{display:flex;align-items:center;gap:5px;background:#fff;padding:2px 7px;border-radius:2px}
  .brand i{width:10px;height:10px;border-radius:50%;background:var(--orange);display:block}
  .brand span{font-size:11px;font-weight:700;color:var(--blue);letter-spacing:.5px}
  .intro{font-size:12.5px;line-height:17px;margin-top:12px;text-align:justify}
  .bullets{list-style:none;margin-top:16px}
  .bullets li{position:relative;padding-left:18px;font-size:12.5px;line-height:17px;margin-bottom:14px}
  .bullets li::before{content:"";position:absolute;left:2px;top:5px;width:8px;height:8px;background:var(--green)}
  .media{position:absolute;display:flex;align-items:center;justify-content:center;font-size:11px;color:#fff;text-align:center}
  .media--chillers{left:10px;top:456px;width:350px;height:110px;background:linear-gradient(90deg,#8e969c,#c9ced2 50%,#9aa3a8)}
  .media--network{left:10px;top:576px;width:350px;height:254px;background:linear-gradient(#f4f6f8,#e3e8ec);color:#7a838b;border:1px solid #d6dce1}
  .phase{margin-top:16px}
  .phase:first-of-type{margin-top:12px}
  .phase h3{font-size:13px;font-weight:700;color:var(--navy);line-height:18px}
  .phase h4{font-size:13px;font-weight:700;color:var(--blue);line-height:18px}
  .phase ol{list-style:none;font-size:12.5px;line-height:20px}
  .media--equipment{left:240px;top:700px;width:115px;height:130px;background:linear-gradient(#a7b2bb,#6f7c87)}
  .note{font-size:12px;line-height:16px;margin-top:10px}
  .case-title{font-size:13px;font-weight:700;color:var(--orange);font-style:italic;margin-top:8px}
  .facility{font-size:14px;font-weight:700;color:var(--navy);line-height:18px;margin-top:2px}
  .panel--cases .bullets{margin-top:8px}
  .panel--cases .bullets li{font-size:12px;line-height:15px;margin-bottom:9px}
  .chart{position:absolute;left:20px;width:340px;background:#fff;border:1px solid #c9ced3}
  .chart--bars{top:392px;height:190px}
  .chart--lines{top:604px;height:226px}
  .chart-caption{position:absolute;top:586px;left:20px;width:340px;text-align:center;font-size:10px;font-style:italic;color:var(--text);line-height:14px}
  .wave{position:absolute;left:0;top:850px;width:1200px;height:60px}
  .fold-label{position:absolute;top:930px;font-size:13px;color:#222}
</style>
</head>
<body>

<section class="panel panel--services">
  <header class="panel-head"><h2>SERVICES</h2><div class="brand"><i></i><span>CORVALITH</span></div></header>
  <p class="intro">CORVALITH's highly educated and experienced staff can provide any and all of the following services with special attention to the type of facility. The uniqueness of each facility type requires the correct expertise to meet both thermal comfort requirements and the need for energy efficiency.</p>
  <ul class="bullets">
    <li>HVAC Engineering Consulting</li>
    <li>Investment-Grade Energy Audits</li>
    <li>New Building Commissioning and Re-Commissioning</li>
    <li>Building Retrofits and Integrated Energy System Commissioning and Optimization (IBESCO)</li>
    <li>Kelvra Rating Certification</li>
    <li>Measurement and Verification (M&amp;V)</li>
    <li>Training and Documentation</li>
  </ul>
  <div class="media media--chillers" role="img" aria-label="Photo of industrial chillers and air handling units"></div>
  <div class="media media--network" role="img" aria-label="Diagram of a building automation system network with controllers and field devices">Building automation system network</div>
</section>

<section class="panel panel--procedure">
  <header class="panel-head"><h2>PROCEDURE</h2><div class="brand"><i></i><span>CORVALITH</span></div></header>
  <div class="phase"><h3>Phase 1:</h3><h4>Preliminary Studies</h4>
    <ol><li>1. Compare and analyze energy use index by building types</li><li>2. Use Kelvra Rating, TMES Standard 90.1</li><li>3. Preliminary work-through</li><li>4. Evaluate economic values of the projects</li></ol></div>
  <div class="phase"><h3>Phase 2:</h3><h4>Energy Audits</h4>
    <ol><li>1. Collect and analyze existing documents</li><li>2. Interview with site staffs</li><li>3. On-site evaluation for 2~5 days</li><li>4. Calculate energy savings</li><li>5. Provide audit reports and proposals</li></ol></div>
  <div class="phase"><h3>Phase 3:</h3><h4>Implementation</h4>
    <ol><li>1. Kick-off meeting with onsite staff's approval</li><li>2. Retrofit specs, bids, installations</li><li>3. Functional tests for new equipment</li><li>4. Optimization and custom algorithm</li><li>5. End of work report</li></ol></div>
  <div class="phase"><h3>Phase 4:</h3><h4>M&amp;V</h4>
    <ol><li>1.Immediate checks for results</li><li>2. Seasonal check-ups</li><li>3. Long-term M&amp;V for building energy usage</li><li>4. Final report</li><li>5. Case studies and benchmarking</li></ol></div>
  <div class="media media--equipment" role="img" aria-label="Photo of mechanical room equipment"></div>
</section>

<section class="panel panel--cases">
  <header class="panel-head"><h2>CASE STUDIES</h2><div class="brand"><i></i><span>CORVALITH</span></div></header>
  <p class="note">(The case studies listed below were summaries of Dr. Kal's engineering performance during his career.)</p>
  <p class="case-title">Case Study 1</p>
  <p class="facility">Facility: A semiconductor technology company in Dallas, Texas</p>
  <ul class="bullets">
    <li>A campus of 8 buildings with offices and labs</li>
    <li>1,200,000 square feet. total</li>
    <li>97 Single Duct VAV AHU and 55 Single Zone AHU</li>
    <li>2,255 VAV terminal boxes and 57 fan powered boxes</li>
    <li>Chilled water is supplied by on-campus central plant</li>
    <li>4 chillers: 2 chillers @1200 ton, 2 chillers @900 ton</li>
    <li>2.7 million gallon thermal storage tank (chilled water)</li>
  </ul>
  <svg class="chart chart--bars" viewBox="0 0 340 190" role="img" aria-label="Monthly energy usage bar chart">
    <text x="170" y="15" font-size="9" fill="#c0392b" text-anchor="middle" font-family="Open Sans,sans-serif">EUPW Usage w/o Datacenter</text>
    <line x1="30" y1="160" x2="330" y2="160" stroke="#999"/><line x1="30" y1="24" x2="30" y2="160" stroke="#999"/>
    <g fill="#3a67b5">
      <rect x="36" y="70" width="8" height="90"/><rect x="48" y="76" width="8" height="84"/><rect x="60" y="68" width="8" height="92"/><rect x="72" y="62" width="8" height="98"/>
      <rect x="84" y="56" width="8" height="104"/><rect x="96" y="52" width="8" height="108"/><rect x="108" y="50" width="8" height="110"/><rect x="120" y="54" width="8" height="106"/>
      <rect x="132" y="62" width="8" height="98"/><rect x="144" y="72" width="8" height="88"/><rect x="156" y="76" width="8" height="84"/><rect x="168" y="74" width="8" height="86"/>
    </g>
    <g fill="#c0392b">
      <rect x="186" y="94" width="8" height="66"/><rect x="198" y="98" width="8" height="62"/><rect x="210" y="92" width="8" height="68"/><rect x="222" y="88" width="8" height="72"/>
      <rect x="234" y="84" width="8" height="76"/><rect x="246" y="80" width="8" height="80"/><rect x="258" y="78" width="8" height="82"/><rect x="270" y="82" width="8" height="78"/>
      <rect x="282" y="88" width="8" height="72"/><rect x="294" y="94" width="8" height="66"/><rect x="306" y="98" width="8" height="62"/><rect x="318" y="96" width="8" height="64"/>
    </g>
    <text x="170" y="178" font-size="8" fill="#666" text-anchor="middle" font-family="Open Sans,sans-serif">Month (before / after)</text>
  </svg>
  <p class="chart-caption">Case Study 1</p>
  <svg class="chart chart--lines" viewBox="0 0 340 226" role="img" aria-label="Daily total electricity profile line chart">
    <text x="200" y="16" font-size="9" fill="#333" text-anchor="middle" font-family="Open Sans,sans-serif">Daily total electricity profile</text>
    <line x1="30" y1="196" x2="330" y2="196" stroke="#999"/><line x1="30" y1="26" x2="30" y2="196" stroke="#999"/>
    <polyline fill="none" stroke="#c0392b" stroke-width="2" points="30,55 60,58 90,55 120,60 150,63 180,85 190,140 220,145 250,142 280,143 300,100 315,58 330,55"/>
    <polyline fill="none" stroke="#4a9a3a" stroke-width="2" points="30,74 60,77 90,74 120,78 150,79 180,82 210,79 240,80 270,78 300,79 330,76"/>
    <polyline fill="none" stroke="#3a67b5" stroke-width="2" points="30,150 60,153 90,149 120,151 150,154 180,150 210,153 240,151 270,154 300,150 330,151"/>
    <text x="180" y="214" font-size="8" fill="#666" text-anchor="middle" font-family="Open Sans,sans-serif">Hour of the day</text>
  </svg>
</section>

<svg class="wave" viewBox="0 0 1200 60" preserveAspectRatio="none" aria-hidden="true">
  <path d="M0,22 C300,0 600,44 900,16 C1020,6 1120,10 1200,16 L1200,60 L0,60 Z" fill="var(--sky)"/>
  <path d="M0,32 C300,12 600,54 900,28 C1020,19 1120,22 1200,28 L1200,60 L0,60 Z" fill="var(--blue)"/>
  <path d="M0,44 C300,28 600,62 900,40 C1020,34 1120,36 1200,40 L1200,60 L0,60 Z" fill="var(--green)"/>
</svg>

<span class="fold-label" style="left:170px">Inside 1</span>
<span class="fold-label" style="left:585px">Inside2</span>
<span class="fold-label" style="left:985px">Inside3</span>

</body>
</html>
```